Office Building Banner

Need a 4x8 vinyl banner made for our office/storage headquarters. Our branded colors and logo can be taken from our website, www.halvenroofingtx.com. All other elements of our brand have not been decided on yet, so you have creative autonomy there. Our location faces a busy highway in Seguin, Texas, so the banner needs to have our contact information and full name clearly seen from a bit away's away, hope that makes sense. Our company wants to convey attributes of strength, loyalty, protection - basically emulating the qualities of a wolf and his pack. I have uploaded a few items we have been using to date, but as you can see, graphic design is not our forte.

```html
<!DOCTYPE html>
<html lang="en">
<head>
<meta charset="utf-8">
<title>Halven Roofing &amp; Renovations – Services Banner</title>
<link rel="stylesheet" href="https://fonts.googleapis.com/css2?family=Poppins:wght@500;600;700;800&display=swap">
<style>
  :root {
    --canvas: #e9ebee;
    --panel-black: #141414;
    --tile-dark: #1c1c1c;
    --tile-mid: #2a2a2a;
    --orange: #f0731f;
    --orange-deep: #e2561a;
    --grey-chevron: #d9d9d9;
    --white: #ffffff;
  }
  * { margin: 0; padding: 0; box-sizing: border-box; }
  html, body {
    width: 1200px;
    height: 1200px;
    overflow: hidden;
    background: var(--canvas);
    font-family: "Poppins", sans-serif;
  }
  .banner {
    position: absolute;
    left: 30px;
    top: 300px;
    width: 1140px;
    height: 600px;
    overflow: hidden;
    background: var(--panel-black);
  }
  .tile-texture {
    position: absolute;
    left: 360px;
    top: 0;
    width: 780px;
    height: 600px;
    background: linear-gradient(160deg, var(--tile-mid) 0%, var(--tile-dark) 45%, #111 100%);
  }
  .banner-shapes {
    position: absolute;
    inset: 0;
  }
  .brand {
    position: absolute;
    left: 20px;
    top: 0;
    width: 260px;
    height: 600px;
    display: flex;
    flex-direction: column;
    align-items: center;
    justify-content: center;
    gap: 12px;
    padding-top: 40px;
    color: var(--white);
    font-weight: 700;
    text-align: center;
  }
  .brand-mark {
    width: 110px;
    height: 110px;
    border: 4px solid var(--white);
    border-radius: 50%;
  }
  .brand-name {
    font-size: 36px;
    line-height: 1;
    letter-spacing: 1px;
    white-space: nowrap;
  }
  .brand-sub {
    font-size: 13px;
    letter-spacing: 0.5px;
    white-space: nowrap;
  }
  .content {
    position: absolute;
    left: 460px;
    top: 78px;
    width: 640px;
    text-align: center;
  }
  .title {
    color: var(--orange);
    font-weight: 800;
    font-size: 76px;
    line-height: 1;
    letter-spacing: 1px;
  }
  .tagline {
    color: var(--white);
    font-weight: 600;
    font-size: 23px;
    line-height: 1.3;
    margin-top: 14px;
  }
  .services {
    display: flex;
    justify-content: center;
    margin-top: 40px;
  }
  .service {
    width: 210px;
    display: flex;
    flex-direction: column;
    align-items: center;
    gap: 8px;
    color: var(--orange);
    font-weight: 700;
    font-size: 20px;
    line-height: 1.1;
    text-transform: uppercase;
  }
  .service + .service { border-left: 3px solid var(--orange); }
  .service svg { width: 78px; height: 62px; }
  .contact {
    margin-top: 52px;
    font-weight: 700;
    font-size: 32px;
    color: var(--white);
  }
  .contact .call { color: var(--orange); font-weight: 600; }
  .website {
    margin-top: 6px;
    font-weight: 600;
    font-size: 26px;
    color: var(--white);
  }
</style>
</head>
<body>
  <section class="banner">
    <div class="tile-texture" role="img" aria-label="Dark roof shingle texture background"></div>

    <svg class="banner-shapes" viewBox="0 0 1140 600" width="1140" height="600" aria-hidden="true">
      <polygon points="0,0 330,0 420,300 330,600 0,600" fill="var(--panel-black)"/>
      <polygon points="370,0 470,0 400,300 470,600 370,600 440,300" fill="var(--orange-deep)"/>
      <polygon points="290,0 360,0 420,120 350,120" fill="var(--grey-chevron)"/>
      <polygon points="350,120 420,120 360,240 290,240" fill="var(--grey-chevron)"/>
      <polygon points="290,360 360,360 420,480 350,480" fill="var(--grey-chevron)"/>
      <polygon points="350,480 420,480 360,600 290,600" fill="var(--grey-chevron)"/>
    </svg>

    <div class="brand">
      <div class="brand-mark"></div>
      <div class="brand-name">HALVEN LLC</div>
      <div class="brand-sub">ROOFING &amp; RENOVATIONS</div>
    </div>

    <div class="content">
      <h1 class="title">OUR SERVICES</h1>
      <p class="tagline">A total solutions partner for all your home<br>improvements needs</p>

      <div class="services">
        <div class="service">
          <svg viewBox="0 0 78 62" aria-hidden="true">
            <polyline points="4,40 30,14 56,40" fill="none" stroke="var(--orange)" stroke-width="5" stroke-linejoin="round"/>
            <polyline points="26,40 48,18 74,40" fill="none" stroke="var(--orange)" stroke-width="5" stroke-linejoin="round"/>
          </svg>
          <span>Roofing</span>
        </div>
        <div class="service">
          <svg viewBox="0 0 78 62" aria-hidden="true">
            <polygon points="39,4 74,58 4,58" fill="var(--orange)"/>
            <path d="M30 48 L44 32 M40 28 a6 6 0 1 0 8 8" stroke="var(--panel-black)" stroke-width="4" fill="none" stroke-linecap="round"/>
          </svg>
          <span>Turn<br>Services</span>
        </div>
        <div class="service">
          <svg viewBox="0 0 78 62" aria-hidden="true">
            <path d="M16 31 a23 23 0 0 1 42 -13" fill="none" stroke="var(--orange)" stroke-width="5"/>
            <polygon points="62,8 64,24 50,20" fill="var(--orange)"/>
            <path d="M62 31 a23 23 0 0 1 -42 13" fill="none" stroke="var(--orange)" stroke-width="5"/>
            <polygon points="16,54 14,38 28,42" fill="var(--orange)"/>
            <path d="M29 32 L39 23 L49 32 V42 H29 Z" fill="var(--orange)"/>
          </svg>
          <span>Renovations</span>
        </div>
      </div>

      <p class="contact"><span class="call">Call Us Today</span> 512-555-0148</p>
      <p class="website">www.halvenroofingtx.com</p>
    </div>
  </section>
</body>
</html>
```